Medical Device Packaging Project 1 of 5

We are a medical device startup company needing packaging for a total of 5 device brands. This is posting 1 of 5 and the device name is "Mirovent"

Mirovent is an intraocular lens for use in cataract surgery. The target market is Chinese ophthalmologists. The box should be sophisticated and upmarket.

The company name is Tepsico Optics, I have included the logo in the uploaded files section. You should include the logo on the box.

I have uploaded a sample lens boxes from other companies that demonstrate the information needed to be contained on the box in terms of address, warnings, symbols, etc.

I have also uploaded the blank dieline of the boxes

You are welcome and encouraged to also submit to projects 2, 3, 4, and 5 as well. The same rules and expectations apply.

Requirements
Should not have
• Should not have any images of an eye or any bionic/futuristic feel to the design
• Note that the valdrimex box is for text reference only. You may use the lens image but the futuristic/bionic look is NOT what we are going for with this brand. It should be traditional upmarket medical device artwork.

```html
<!DOCTYPE html>
<html lang="en">
<head>
<meta charset="utf-8">
<title>Mirovent – Tepsico Optics Lens Box Panels</title>
<link rel="stylesheet" href="https://fonts.googleapis.com/css2?family=Montserrat:wght@500;600&family=Arimo:wght@400&display=swap">
<style>
  :root {
    --page-bg: #ececec;
    --panel-light: #e6f4f9;
    --panel-mid: #b3e0ee;
    --panel-deep: #74c6de;
    --ink-navy: #1d3f7c;
    --ink-text: #234a86;
    --lens-light: #f2f2f2;
    --lens-mid: #9a9a9a;
    --lens-dark: #5e5e5e;
  }
  * { margin: 0; padding: 0; box-sizing: border-box; }
  html, body { width: 1200px; height: 782px; overflow: hidden; }
  body {
    background: var(--page-bg);
    font-family: "Montserrat", sans-serif;
    color: var(--ink-navy);
    position: relative;
  }
  .panel {
    position: absolute;
    top: 190px;
    width: 530px;
    height: 400px;
    background: linear-gradient(135deg, var(--panel-light) 0%, var(--panel-mid) 55%, var(--panel-deep) 100%);
    overflow: hidden;
  }
  .panel--back { left: 40px; }
  .panel--front { left: 630px; }

  .brand {
    position: absolute;
    top: 38px;
    right: 34px;
    display: flex;
    align-items: center;
    gap: 8px;
    font-weight: 500;
    font-size: 17px;
    letter-spacing: 1.5px;
    color: var(--ink-navy);
    text-transform: uppercase;
  }
  .brand__dot {
    width: 14px; height: 14px;
    border: 2px solid var(--ink-navy);
    border-radius: 50%;
  }

  .product-title {
    position: absolute;
    left: 32px;
    font-weight: 600;
    font-size: 16px;
    line-height: 22px;
    letter-spacing: 0.3px;
    text-transform: uppercase;
    color: var(--ink-navy);
  }
  .panel--back .product-title { top: 100px; }
  .panel--front .product-title { top: 100px; }

  .lens-art {
    position: absolute;
    border-radius: 50%;
    background: radial-gradient(circle at 40% 35%, var(--lens-light) 0%, var(--lens-mid) 55%, var(--lens-dark) 100%);
  }
  .panel--back .lens-art { left: 70px; top: 190px; width: 130px; height: 130px; }
  .panel--front .lens-art { left: 140px; top: 140px; width: 160px; height: 160px; }

  .warnings {
    position: absolute;
    left: 312px;
    top: 142px;
    width: 210px;
    font-family: "Arimo", sans-serif;
    font-size: 6.8px;
    line-height: 7.6px;
    color: var(--ink-text);
  }
  .warnings p { margin-bottom: 2px; }

  .symbols {
    position: absolute;
    left: 312px;
    bottom: 26px;
    display: flex;
    align-items: center;
    gap: 10px;
  }
  .symbols__sterile {
    font-family: "Arimo", sans-serif;
    font-size: 6px;
    border: 1px solid var(--ink-text);
    color: var(--ink-text);
    padding: 2px 3px;
    display: flex;
    gap: 3px;
  }
  .symbols svg { display: block; }

  .device-name {
    position: absolute;
    right: 34px;
    bottom: 58px;
    font-weight: 600;
    font-size: 26px;
    letter-spacing: 3px;
    text-transform: uppercase;
    color: var(--ink-navy);
  }
  .device-sub {
    position: absolute;
    right: 34px;
    bottom: 38px;
    font-weight: 500;
    font-size: 15px;
    letter-spacing: 0.4px;
    text-transform: uppercase;
    color: var(--ink-navy);
  }
</style>
</head>
<body>

<section class="panel panel--back" aria-label="Box back panel">
  <div class="brand"><span class="brand__dot"></span>Tepsico Optics</div>
  <h2 class="product-title">Hydrophobic intraocular lens<br>Aspheric with 360° lens</h2>
  <div class="lens-art" role="img" aria-label="Illustration of the intraocular lens with curved haptics"></div>
  <div class="warnings">
    <p>Contains one sterile intraocular lens<br>Do not use if the packaging is damaged<br>Do not resterilize</p>
    <p>Bevat één steriele intraoculaire lens<br>Niet gebruiken als de verpakking beschadigd is<br>Niet opnieuw steriliseren</p>
    <p>Contient une lentille intraoculaire stérile<br>Ne pas utiliser si l'emballage est endommagé<br>Ne pas restériliser</p>
    <p>Enthält eine sterile Intraokulare Linse<br>Nicht verwenden, wenn die Verpackung beschädigt ist<br>Nicht resterilisieren</p>
    <p>Περιέχει ένα αποστειρωμένο ενδοφθάλμιο φακό<br>Μην το χρησιμοποιείτε εάν η συσκευασία έχει φθαρεί<br>Μην επαναποστειρώνετε</p>
    <p>Contiene una lente intraoculare sterile<br>Non usare se la confezione è danneggiata<br>Non risterilizzare</p>
    <p>Contém uma lente intra-ocular esterilizada<br>Não use se a embalagem está danificada<br>Não reesterilize</p>
    <p>Contiene una lente intraocular estéril<br>No utilizar si el envase está dañado<br>No vuelva a esterilizar</p>
  </div>
  <div class="symbols">
    <span class="symbols__sterile"><span>STERILE</span><span>EO</span></span>
    <svg width="16" height="14" viewBox="0 0 16 14" aria-hidden="true"><path d="M8 1 L15 13 H1 Z" fill="none" stroke="#234a86" stroke-width="1"/><line x1="8" y1="5" x2="8" y2="9" stroke="#234a86"/></svg>
    <svg width="14" height="14" viewBox="0 0 14 14" aria-hidden="true"><circle cx="7" cy="7" r="6" fill="none" stroke="#234a86"/><line x1="3" y1="3" x2="11" y2="11" stroke="#234a86"/></svg>
    <svg width="14" height="14" viewBox="0 0 14 14" aria-hidden="true"><circle cx="7" cy="7" r="6" fill="none" stroke="#234a86"/><line x1="3" y1="11" x2="11" y2="3" stroke="#234a86"/></svg>
    <svg width="14" height="14" viewBox="0 0 14 14" aria-hidden="true"><circle cx="7" cy="7" r="6" fill="none" stroke="#234a86"/><circle cx="7" cy="7" r="2.5" fill="none" stroke="#234a86"/></svg>
  </div>
</section>

<section class="panel panel--front" aria-label="Box front panel">
  <div class="brand"><span class="brand__dot"></span>Tepsico Optics</div>
  <h2 class="product-title">Hydrophobic intraocular lens</h2>
  <div class="lens-art" role="img" aria-label="Illustration of the intraocular lens with curved haptics"></div>
  <div class="device-name">Mirovent</div>
  <div class="device-sub">Aspheric with 360° lens</div>
</section>

</body>
</html>
```